Quick 1hr job to create exciting page header & footer designs

We need some exciting and engaging header and footer designs for school yearbooks, in particular for the NZ Primary school market (children 5 to 10 years old).
The header and footer designs need to be bright and colourful, and should appeal to younger children. Header and footer graphics do not need to be the same, but should at least relate to each other thematically.
Please include the following sample text on the header: Sports Day.
Please include this sample text on the footer: Primary School Name 2014.
Note that the header/footers may be used without the text so the design should work with or without the text. Header/footer may be used over top of a coloured or graphic background. The graphic could be illustrative, photographic or patterned, the more creative the better.

Header dimensions: 198.88 mm w x 15.24 mm h
Footer dimensions: 198.88 mm w x 6.35 mm h

Please see the example pages provided, but please note we are looking for something more suitable for Primary Schools, and a lot more dynamic and interesting!

Target Market(s)

New Zealand Primary Schools

Industry/Entity Type

School

Requirements
Must have
• Must contain sample text and must be suitable for younger children
• Must be appropriate for the New Zealand market, i.e. don't use imagery that is obviously from other countries.

```html
<!DOCTYPE html>
<html lang="en">
<head>
<meta charset="utf-8">
<title>Sports Day – Header and Footer Set</title>
<link rel="stylesheet" href="https://fonts.googleapis.com/css2?family=Mystery+Quest&family=Open+Sans:wght@400&display=swap">
<style>
  :root {
    --page: #ffffff;
    --label: #222222;
    --divider: #f4a77a;
    --red: #e8392f;
    --navy: #2b2f92;
    --grass: #8cc63f;
    --pennant: linear-gradient(90deg,#f15a5a 0 8%,#ffd23f 8% 16%,#3fb6e8 16% 24%,#8cc63f 24% 32%,#f27ec2 32% 40%,#ffa23f 40% 48%,#3fb6e8 48% 56%,#ffd23f 56% 64%,#f15a5a 64% 72%,#8cc63f 72% 80%,#b57edc 80% 88%,#ffa23f 88% 100%);
    --flowers: linear-gradient(90deg,#bfe6f5 0%,#ffe2a3 35%,#f9c3de 65%,rgba(255,255,255,0) 100%);
    --squares: linear-gradient(90deg,rgba(255,255,255,0) 0%,#e6f3d0 30%,#cfe9f2 60%,#f6c9e2 85%,#e7d3f3 100%);
  }
  * { box-sizing: border-box; margin: 0; padding: 0; }
  html, body { width: 1200px; height: 617px; overflow: hidden; background: var(--page); }
  body { position: relative; font-family: "Open Sans", sans-serif; }

  .label { position: absolute; left: 70px; font-size: 18px; color: var(--label); }

  .header-band {
    position: absolute; left: 70px; width: 1054px; height: 84px;
    background: var(--page); overflow: hidden;
  }
  .bunting { position: absolute; left: 0; right: 0; top: 0; height: 12px; background: var(--pennant); }
  .grass { position: absolute; left: 0; right: 0; bottom: 0; height: 5px; background: var(--grass); }
  .art-left { position: absolute; left: 0; top: 12px; bottom: 5px; width: 230px; background: var(--flowers); }
  .art-right { position: absolute; right: 0; top: 12px; bottom: 5px; width: 240px; background: var(--squares); }

  .title-row {
    position: absolute; left: 0; right: 0; top: 12px; bottom: 5px;
    display: flex; align-items: center; justify-content: center; gap: 26px;
  }
  .title { font-family: "Mystery Quest", cursive; font-size: 46px; line-height: 1; }
  .stars { font-size: 14px; letter-spacing: 6px; line-height: 1; }
  .stars .big { font-size: 24px; letter-spacing: 0; }

  .footer-band { position: absolute; left: 70px; width: 1054px; height: 40px; }
  .footer-band .bunting { height: 8px; }
  .footer-row {
    position: absolute; left: 0; right: 0; top: 12px;
    display: flex; align-items: center; justify-content: center; gap: 22px;
  }
  .footer-text { font-family: "Mystery Quest", cursive; font-size: 19px; line-height: 1; }
  .footer-row .stars { font-size: 11px; }
  .footer-row .stars .big { font-size: 19px; }

  .theme-red { color: var(--red); }
  .theme-navy { color: var(--navy); }

  .divider { position: absolute; left: 70px; width: 1052px; top: 307px; border-top: 2px solid var(--divider); }
</style>
</head>
<body>

  <p class="label" style="top:26px">Header</p>
  <section class="header-band theme-red" style="top:57px">
    <div class="bunting" role="img" aria-label="Row of colourful bunting pennants"></div>
    <div class="art-left" role="img" aria-label="Bright pastel flower illustration"></div>
    <div class="art-right" role="img" aria-label="Playful overlapping coloured squares"></div>
    <div class="title-row">
      <span class="stars">★★★★<span class="big">★</span></span>
      <h1 class="title">Sports Day</h1>
      <span class="stars"><span class="big">★</span>★★★★</span>
    </div>
    <div class="grass" role="img" aria-label="Green grass edge"></div>
  </section>

  <p class="label" style="top:192px">Footer</p>
  <section class="footer-band theme-red" style="top:216px">
    <div class="bunting" role="img" aria-label="Row of colourful bunting pennants"></div>
    <div class="footer-row">
      <span class="stars">★★★★<span class="big">★</span></span>
      <p class="footer-text">Primary School Name - 2014</p>
      <span class="stars"><span class="big">★</span>★★★★</span>
    </div>
  </section>

  <hr class="divider">

  <p class="label" style="top:338px">Header</p>
  <section class="header-band theme-navy" style="top:369px">
    <div class="bunting" role="img" aria-label="Row of colourful bunting pennants"></div>
    <div class="art-left" role="img" aria-label="Bright pastel flower illustration"></div>
    <div class="art-right" role="img" aria-label="Playful overlapping coloured squares"></div>
    <div class="title-row">
      <span class="stars">★★★★<span class="big">★</span></span>
      <h1 class="title">Sports Day</h1>
      <span class="stars"><span class="big">★</span>★★★★</span>
    </div>
    <div class="grass" role="img" aria-label="Green grass edge"></div>
  </section>

  <p class="label" style="top:500px">Footer</p>
  <section class="footer-band theme-navy" style="top:526px">
    <div class="bunting" role="img" aria-label="Row of colourful bunting pennants"></div>
    <div class="footer-row">
      <span class="stars">★★★★<span class="big">★</span></span>
      <p class="footer-text">Primary School Name - 2014</p>
      <span class="stars"><span class="big">★</span>★★★★</span>
    </div>
  </section>

</body>
</html>
```